InfoGraphic for Security Pyramid

I've created an infographic that I would like to be redone more professionally. you can see the page in this powerpoint called the pyramid of security. What I'd like done is to replace the background graphic with a new icon in a cartoony format like the one behind end point protection as an example (thats a stock photo).

Target Market(s)

Business Owners

Font styles to use
Sans Serif

Colors
ec1f27
0355a3
f37122

Requirements
Must have
• Consistent images, text must be editable.

```html
<!DOCTYPE html>
<html lang="en">
<head>
<meta charset="utf-8">
<title>Pyramid of Security</title>
<link rel="stylesheet" href="https://fonts.googleapis.com/css2?family=Open+Sans:wght@400;600&display=swap">
<style>
  :root {
    --tier-awareness: #5b9bd5;
    --tier-monitoring: #e0711e;
    --tier-insight: #a5a5a5;
    --tier-defence: #db3f3f;
    --tier-foundation: #5b9bd5;
    --line: #ffffff;
    --page: #ffffff;
  }
  html, body {
    margin: 0;
    padding: 0;
    width: 1200px;
    height: 1200px;
    overflow: hidden;
    background: var(--page);
    font-family: "Open Sans", sans-serif;
  }
  .pyramid {
    position: relative;
    width: 1200px;
    height: 1200px;
  }
  .tier {
    position: absolute;
    display: flex;
    height: 229px;
  }
  .tile {
    position: relative;
    width: 228px;
    height: 229px;
    box-sizing: border-box;
    border: 1px solid var(--line);
  }
  .tile-icon {
    position: absolute;
    left: 24px;
    top: 24px;
    width: 180px;
    height: 180px;
    fill: none;
    stroke: var(--line);
    stroke-width: 1.4;
    stroke-linejoin: round;
    stroke-linecap: round;
  }
  .tile-icon .solid { fill: var(--line); stroke: none; }
  .tile-icon .dashed { stroke-dasharray: 3 2.5; }
  .tile-label {
    position: absolute;
    width: 1px;
    height: 1px;
    overflow: hidden;
    clip: rect(0 0 0 0);
    white-space: nowrap;
    font-size: 16px;
    font-weight: 600;
    color: var(--line);
  }
  .tier-awareness  { left: 486px; top: 21px; }
  .tier-monitoring { left: 371px; top: 249px; }
  .tier-insight    { left: 257px; top: 478px; }
  .tier-defence    { left: 143px; top: 708px; }
  .tier-foundation { left: 29px;  top: 938px; }
  .tier-awareness .tile  { background: var(--tier-awareness); }
  .tier-monitoring .tile { background: var(--tier-monitoring); }
  .tier-insight .tile    { background: var(--tier-insight); }
  .tier-defence .tile    { background: var(--tier-defence); }
  .tier-foundation .tile { background: var(--tier-foundation); }
  .tier-defence .badge-fill { fill: var(--tier-defence); }
</style>
</head>
<body>
<main class="pyramid" aria-label="Pyramid of security">

  <section class="tier tier-awareness">
    <div class="tile">
      <span class="tile-label">Security Awareness Training</span>
      <svg class="tile-icon" viewBox="0 0 100 100" aria-hidden="true">
        <rect x="40" y="26" width="44" height="28"/>
        <line x1="42" y1="59" x2="82" y2="59"/>
        <polygon points="16,50 42,50 38,74 20,74"/>
        <line x1="16" y1="78" x2="42" y2="78"/>
        <line x1="36" y1="46" x2="56" y2="36"/>
      </svg>
    </div>
  </section>

  <section class="tier tier-monitoring">
    <div class="tile">
      <span class="tile-label">Log Management</span>
      <svg class="tile-icon" viewBox="0 0 100 100" aria-hidden="true">
        <path d="M14 30 H56 L40 50 V72 L32 66 V50 Z"/>
        <line x1="14" y1="40" x2="58" y2="40"/>
        <line x1="60" y1="30" x2="60" y2="66"/>
        <line x1="60" y1="48" x2="68" y2="30"/>
        <line x1="60" y1="48" x2="68" y2="48"/>
        <line x1="60" y1="48" x2="68" y2="66"/>
        <rect x="68" y="24" width="20" height="12"/>
        <rect x="68" y="42" width="20" height="12"/>
        <rect x="68" y="60" width="20" height="12"/>
      </svg>
    </div>
    <div class="tile">
      <span class="tile-label">Threat Detection</span>
      <svg class="tile-icon" viewBox="0 0 100 100" aria-hidden="true">
        <circle cx="50" cy="50" r="34"/>
        <circle cx="50" cy="50" r="25"/>
        <circle cx="50" cy="50" r="16" class="dashed"/>
        <line x1="50" y1="50" x2="76" y2="24"/>
        <circle class="solid" cx="50" cy="50" r="2.4"/>
        <circle class="solid" cx="40" cy="21" r="2.6"/>
        <circle class="solid" cx="71" cy="63" r="2.6"/>
        <circle class="solid" cx="26" cy="62" r="2.6"/>
      </svg>
    </div>
  </section>

  <section class="tier tier-insight">
    <div class="tile">
      <span class="tile-label">Risk Assessment</span>
      <svg class="tile-icon" viewBox="0 0 100 100" aria-hidden="true">
        <polygon points="50,24 72,58 28,58"/>
        <line x1="50" y1="36" x2="50" y2="47"/>
        <circle class="solid" cx="50" cy="52" r="1.8"/>
        <line x1="12" y1="60" x2="88" y2="60"/>
        <polyline class="dashed" points="32,62 50,84 68,62"/>
      </svg>
    </div>
    <div class="tile">
      <span class="tile-label">Network Mapping</span>
      <svg class="tile-icon" viewBox="0 0 100 100" aria-hidden="true">
        <circle cx="50" cy="54" r="10"/>
        <circle cx="48" cy="22" r="6"/>
        <circle cx="76" cy="32" r="5"/>
        <circle cx="84" cy="56" r="6"/>
        <circle cx="18" cy="54" r="8"/>
        <circle cx="30" cy="78" r="6"/>
        <circle cx="72" cy="78" r="4"/>
        <line x1="49.5" y1="44" x2="48.5" y2="28"/>
        <line x1="57" y1="47" x2="72" y2="35"/>
        <line x1="60" y1="55" x2="78" y2="56"/>
        <line x1="40" y1="54" x2="26" y2="54"/>
        <line x1="43" y1="61" x2="34" y2="73"/>
        <line x1="57" y1="61" x2="69" y2="75"/>
      </svg>
    </div>
    <div class="tile">
      <span class="tile-label">Data Consolidation</span>
      <svg class="tile-icon" viewBox="0 0 100 100" aria-hidden="true">
        <path d="M16 36 V22 H23 L25 25 H36 V36 Z"/>
        <path d="M40 36 V22 H47 L49 25 H60 V36 Z"/>
        <path d="M64 36 V22 H71 L73 25 H84 V36 Z"/>
        <polyline points="26,36 50,54 74,36"/>
        <line x1="50" y1="36" x2="50" y2="58"/>
        <polygon class="solid" points="46,57 54,57 50,62"/>
        <path d="M34 84 V64 H44 L47 68 H66 V84 Z"/>
      </svg>
    </div>
  </section>

  <section class="tier tier-defence">
    <div class="tile">
      <span class="tile-label">Firewall</span>
      <svg class="tile-icon" viewBox="0 0 100 100" aria-hidden="true">
        <rect x="14" y="22" width="72" height="56"/>
        <line x1="14" y1="36" x2="86" y2="36"/>
        <line x1="14" y1="50" x2="86" y2="50"/>
        <line x1="14" y1="64" x2="86" y2="64"/>
        <line x1="32" y1="22" x2="32" y2="36"/>
        <line x1="68" y1="22" x2="68" y2="36"/>
        <line x1="23" y1="36" x2="23" y2="50"/>
        <line x1="77" y1="36" x2="77" y2="50"/>
        <line x1="23" y1="64" x2="23" y2="78"/>
        <line x1="77" y1="64" x2="77" y2="78"/>
        <circle class="badge-fill" cx="50" cy="50" r="19"/>
        <path d="M50 62 C41 60 41 50 47 42 C48 48 52 48 51 40 C58 46 60 58 50 62 Z"/>
        <line x1="37" y1="63" x2="63" y2="37"/>
      </svg>
    </div>
    <div class="tile">
      <span class="tile-label">Mobile Device Security</span>
      <svg class="tile-icon" viewBox="0 0 100 100" aria-hidden="true">
        <rect x="30" y="14" width="40" height="72" rx="5"/>
        <rect x="34" y="22" width="32" height="52"/>
        <circle cx="50" cy="80" r="2.4"/>
        <path d="M50 36 L60 40 V48 C60 55 55 59 50 61 C45 59 40 55 40 48 V40 Z"/>
      </svg>
    </div>
    <div class="tile">
      <span class="tile-label">Security Processes</span>
      <svg class="tile-icon" viewBox="0 0 100 100" aria-hidden="true">
        <rect x="12" y="43" width="18" height="14" rx="2"/>
        <polygon points="50,40 60,50 50,60 40,50"/>
        <rect x="70" y="43" width="18" height="14" rx="2"/>
        <rect x="41" y="72" width="18" height="12" rx="2"/>
        <line x1="30" y1="50" x2="36" y2="50"/>
        <polygon class="solid" points="36,47 36,53 40,50"/>
        <line x1="60" y1="50" x2="66" y2="50"/>
        <polygon class="solid" points="66,47 66,53 70,50"/>
        <line x1="50" y1="60" x2="50" y2="68"/>
        <polygon class="solid" points="47,68 53,68 50,72"/>
      </svg>
    </div>
    <div class="tile">
      <span class="tile-label">Compliance</span>
      <svg class="tile-icon" viewBox="0 0 100 100" aria-hidden="true">
        <rect x="26" y="16" width="48" height="68" rx="2"/>
        <rect x="32" y="26" width="10" height="10" rx="1.5"/>
        <rect x="32" y="45" width="10" height="10" rx="1.5"/>
        <rect x="32" y="64" width="10" height="10" rx="1.5"/>
        <polyline points="34,31 37,34 43,25"/>
        <polyline points="34,50 37,53 43,44"/>
        <polyline points="34,69 37,72 43,63"/>
        <line x1="48" y1="31" x2="68" y2="31"/>
        <line x1="48" y1="50" x2="68" y2="50"/>
        <line x1="48" y1="69" x2="68" y2="69"/>
      </svg>
    </div>
  </section>

  <section class="tier tier-foundation">
    <div class="tile">
      <span class="tile-label">Patch Management</span>
      <svg class="tile-icon" viewBox="0 0 100 100" aria-hidden="true">
        <circle cx="50" cy="50" r="31" stroke-width="6" stroke-dasharray="6 6.17"/>
        <circle cx="50" cy="50" r="27"/>
        <path d="M62 38 A17 17 0 1 0 67 52"/>
        <polygon class="solid" points="58,34 66,34 64,42"/>
        <circle cx="50" cy="50" r="7"/>
      </svg>
    </div>
    <div class="tile">
      <span class="tile-label">Access Control</span>
      <svg class="tile-icon" viewBox="0 0 100 100" aria-hidden="true">
        <path d="M35 44 V36 A15 15 0 0 1 65 36 V44"/>
        <path d="M40 44 V37 A10 10 0 0 1 60 37 V44"/>
        <rect x="28" y="44" width="44" height="38"/>
        <circle cx="50" cy="53" r="3"/>
        <line x1="50" y1="56" x2="50" y2="62"/>
        <rect x="32" y="67" width="36" height="9" rx="2"/>
        <circle class="solid" cx="36" cy="71.5" r="1.4"/>
        <line class="dashed" x1="40" y1="71.5" x2="65" y2="71.5"/>
      </svg>
    </div>
    <div class="tile">
      <span class="tile-label">Backup and Recovery</span>
      <svg class="tile-icon" viewBox="0 0 100 100" aria-hidden="true">
        <rect x="16" y="22" width="40" height="14" rx="2"/>
        <rect x="16" y="43" width="40" height="14" rx="2"/>
        <rect x="16" y="64" width="40" height="14" rx="2"/>
        <rect x="21" y="26" width="5" height="5"/>
        <rect x="21" y="47" width="5" height="5"/>
        <rect x="21" y="68" width="5" height="5"/>
        <path d="M82 50 A16 16 0 1 1 70 34.5"/>
        <polygon class="solid" points="68,30 76,35 68,39"/>
      </svg>
    </div>
    <div class="tile">
      <span class="tile-label">Endpoint Protection</span>
      <svg class="tile-icon" viewBox="0 0 100 100" aria-hidden="true">
        <rect x="14" y="22" width="72" height="46"/>
        <line x1="50" y1="68" x2="50" y2="78"/>
        <line x1="34" y1="78" x2="66" y2="78"/>
        <path d="M50 30 L62 35 V45 C62 53 56 57 50 60 C44 57 38 53 38 45 V35 Z"/>
      </svg>
    </div>
    <div class="tile">
      <span class="tile-label">Email Security</span>
      <svg class="tile-icon" viewBox="0 0 100 100" aria-hidden="true">
        <path d="M50 14 L78 24 V48 C78 68 64 80 50 86 C36 80 22 68 22 48 V24 Z"/>
        <rect x="34" y="42" width="32" height="22"/>
        <polyline points="34,42 50,54 66,42"/>
        <line x1="34" y1="64" x2="46" y2="52"/>
        <line x1="66" y1="64" x2="54" y2="52"/>
      </svg>
    </div>
  </section>

</main>
</body>
</html>
```